Redesign web application

we are a tele health start up. we need a new design for our platform that allows users, their family and docs to access their detailed stats online
users take readings using our wireless devices that transmit the readings to our server in the background All this happens in real time . and users can instantly login to the portal to view readings , make comments, , view charts,
if readings are not within in prescribed thresholds then alerts are reported on the website, SMS and email
please see the screenshots of existing pages
We need the following pages re designed
login page
patient DB summary , patient DB condition
Doc DB
Nurse DB
After you submit designs and we choose the winning design . please help to make minor modifications after that so that we can use it
Target Market(s)
Paying
Doctors/ Clinics/Clinic chains/ Specialists will be the ones who are paying for the service. the service
Non Paying
patients family members, doctors all will be accessing the system to view readings, alerts , make comments , see charts
Industry/Entity Type
Health
Colors
Designer to choose colors to be used in the design.
Look and feel

```html
<!DOCTYPE html>
<html lang="en">
<head>
<meta charset="utf-8">
<title>VitaLink Dashboard</title>
<link href="https://fonts.googleapis.com/css2?family=Lato:wght@400;700;900&display=swap" rel="stylesheet">
<style>
:root{
  --green:#8cc63f;
  --green-dark:#7ab332;
  --bg:#ebebeb;
  --dark:#333333;
  --nav-line:#4a4a4a;
  --text:#2b2b2b;
  --muted:#555555;
  --link:#4a9fd8;
  --blue:#6ab4d6;
  --yellow:#f0e17a;
  --white:#ffffff;
  --rule:#dcdcdc;
}
*{box-sizing:border-box;margin:0;padding:0}
html,body{width:1200px;height:921px;overflow:hidden}
body{font-family:'Lato',sans-serif;background:var(--bg);color:var(--text);position:relative;font-size:13px}
a{color:var(--link)}
.abs{position:absolute}

/* header */
.topbar{left:0;top:0;width:1200px;height:62px;background:linear-gradient(#ffffff,#f1f1f1);border-bottom:1px solid #d6d6d6}
.brand{left:174px;top:16px;font-size:26px;font-weight:900;color:var(--dark);letter-spacing:.5px;display:flex;align-items:center;gap:7px}
.brand .dot{width:12px;height:12px;background:var(--green);border-radius:50%}
.search{left:494px;top:21px;width:220px;height:25px;border:1px solid #cfcfcf;border-radius:6px;background:#fff;padding:0 14px;font-size:13px;color:#b8b8b8;line-height:23px}
.search svg{position:absolute;right:10px;top:5px}
.messages{left:735px;top:0;width:117px;height:62px;border-left:1px solid #d6d6d6;border-right:1px solid #d6d6d6}
.messages .label{position:absolute;left:14px;top:26px;font-size:12px;font-weight:700;display:flex;gap:6px;align-items:center}
.messages .badge{position:absolute;left:72px;top:12px;background:var(--link);color:#fff;font-size:10px;padding:1px 5px;border-radius:2px}
.caret{width:0;height:0;border-left:4px solid transparent;border-right:4px solid transparent;border-top:5px solid #333;display:inline-block}
.messages .caret{position:absolute;left:95px;top:36px}
.user{left:861px;top:14px;display:flex;gap:12px}
.avatar{width:31px;height:34px;position:relative}
.user .name{font-size:12px;font-weight:700;line-height:16px;margin-top:2px}
.user .sub{font-size:12px;color:var(--muted);display:flex;align-items:center;gap:6px}

/* nav */
.mainnav{left:0;top:62px;width:1200px;height:36px;background:var(--dark)}
.mainnav ul{position:absolute;left:171px;top:0;display:flex;list-style:none}
.mainnav li{height:36px;line-height:36px;text-align:center;color:#fff;font-weight:700;font-size:14px;border-right:1px solid var(--nav-line);position:relative}
.mainnav li:last-child{border-right:none}
.mainnav li.active{background:var(--green)}
.mainnav li.active::after{content:"";position:absolute;left:56px;bottom:0;border-left:6px solid transparent;border-right:6px solid transparent;border-bottom:5px solid var(--bg)}

/* profile */
.profile{left:171px;top:120px;width:858px;height:148px;background:#fff}
.photo{position:absolute;left:0;top:0;width:147px;height:148px;background:linear-gradient(160deg,#e9e9e9 0%,#c9d5e2 60%,#6d8fb6 100%)}
.pname{position:absolute;left:182px;top:11px;font-size:21px;font-weight:400}
.mon-title{position:absolute;left:185px;top:48px;font-size:12px;font-weight:700}
.mon{position:absolute;top:68px;font-size:12px;line-height:19px}
.mon div{display:flex;gap:10px}
.mon .n{width:14px;text-align:right}
.group{position:absolute;left:441px;top:16px;font-size:12px;color:var(--muted)}
.actions{position:absolute;left:456px;top:48px;list-style:none;font-size:12px;color:var(--muted);line-height:23px}
.actions li{display:flex;align-items:center;gap:10px}
.completeness{position:absolute;left:633px;top:16px}
.completeness h3{font-size:12px;font-weight:700}
.ring{position:absolute;left:0;top:30px}
.steps{position:absolute;left:75px;top:32px;list-style:none;font-size:12px;color:var(--muted);line-height:20px;width:150px}
.steps li::before{content:"";display:inline-block;border-top:3px solid transparent;border-bottom:3px solid transparent;border-left:4px solid #555;margin-right:6px;vertical-align:1px}

/* side menus */
.sidemenu{left:171px;width:137px;background:linear-gradient(90deg,#fafafa,#e4e4e4);border:1px solid #e0e0e0;list-style:none}
.sidemenu li{height:34px;display:flex;align-items:center;gap:12px;padding-left:8px;font-size:14px;border-bottom:1px solid #d6d6d6;position:relative}
.sidemenu li svg{flex:none}
.sidemenu li.active{background:var(--green);color:#fff;width:137px;border-bottom:none}
.sidemenu li.active::after{content:"";position:absolute;right:-17px;top:0;border-top:17px solid transparent;border-bottom:17px solid transparent;border-left:17px solid var(--green)}

/* widgets */
.widget{width:325px;height:239px;background:#fff}
.w-head{position:absolute;left:21px;top:12px;font-size:14px;line-height:18px}
.w-head b{font-weight:700}
.w-tools{position:absolute;right:30px;top:18px;display:flex;gap:14px}
.alerts{position:absolute;left:0;top:50px;width:325px;border-top:4px solid var(--blue)}
.alerts table{width:100%;border-collapse:collapse;font-size:11.5px}
.alerts td{height:25px;border-bottom:1px solid var(--rule);padding:0}
.alerts td:first-child{padding-left:21px;width:68px}
.viewall{position:absolute;right:27px;top:200px;font-size:11px;color:var(--green-dark)}
.pie{position:absolute;left:14px;top:58px}
.legend{position:absolute;left:195px;list-style:none;font-size:12.5px;line-height:25px}
.legend li{display:flex;align-items:center;gap:12px}
.legend i{width:8px;height:8px;display:inline-block}

/* footer */
.footer{left:0;top:854px;width:1200px;height:67px;background:var(--dark);color:#ddd;font-size:12px}
.footer .copy{position:absolute;left:177px;top:27px}
.social{position:absolute;left:930px;top:26px;display:flex;gap:12px}
.social span{width:16px;height:16px;border-radius:50%;background:#777}
</style>
</head>
<body>

<header class="abs topbar">
  <div class="abs brand"><span>VitaLink</span><span class="dot"></span></div>
  <div class="abs search">Search:
    <svg width="14" height="14" viewBox="0 0 14 14"><circle cx="6" cy="6" r="4.5" fill="none" stroke="#222" stroke-width="2"/><line x1="9.3" y1="9.3" x2="13" y2="13" stroke="#222" stroke-width="2.2"/></svg>
  </div>
  <div class="abs messages">
    <span class="badge">5</span>
    <div class="label"><svg width="15" height="11" viewBox="0 0 15 11"><rect width="15" height="11" rx="1" fill="#222"/><path d="M0 1 L7.5 6 L15 1" fill="none" stroke="#fff" stroke-width="1.2"/></svg>Messages</div>
    <span class="caret"></span>
  </div>
  <div class="abs user">
    <svg class="avatar" viewBox="0 0 31 34"><circle cx="15.5" cy="9" r="8" fill="var(--green)"/><path d="M0 34 V26 Q0 18 8 18 H23 Q31 18 31 26 V34Z" fill="var(--green)"/></svg>
    <div><div class="name">Sed Egestas</div><div class="sub">Et bibendum mi vene <span class="caret"></span></div></div>
  </div>
</header>

<nav class="abs mainnav">
  <ul>
    <li class="active" style="width:126px">DashBoard</li>
    <li style="width:239px">Patient DB Summary</li>
    <li style="width:219px">Patient DB Condition</li>
    <li style="width:140px">Doc DB</li>
    <li style="width:134px">Nurse DB</li>
  </ul>
</nav>

<section class="abs profile">
  <div class="photo" role="img" aria-label="Portrait photo of the doctor"></div>
  <h1 class="pname">Mei Lin Tan</h1>
  <h2 class="mon-title">MONITORED PATIENTS</h2>
  <div class="mon" style="left:171px">
    <div><span class="n">7</span><a href="#">Diabetes</a></div>
    <div><span class="n">4</span><a href="#">SPO2</a></div>
    <div><span class="n">12</span><a href="#">Weight</a></div>
  </div>
  <div class="mon" style="left:291px">
    <div><span class="n">27</span><a href="#">Hypertension</a></div>
    <div><span class="n">9</span><a href="#">Temperture</a></div>
  </div>
  <div class="group">VitaLink Demo Group</div>
  <ul class="actions">
    <li><svg width="12" height="10" viewBox="0 0 12 10"><path d="M0 2H4L8 8H12M0 8H4L8 2H12" fill="none" stroke="var(--green)" stroke-width="1.6"/></svg>Device Allocations</li>
    <li><svg width="12" height="12" viewBox="0 0 12 12"><circle cx="6" cy="6" r="4" fill="none" stroke="var(--green)" stroke-width="3" stroke-dasharray="2 1.2"/></svg>Settings</li>
    <li><svg width="12" height="10" viewBox="0 0 12 10"><path d="M0 1H12M3 4H12M3 7H12M0 9.5H12" stroke="var(--green)" stroke-width="1.4"/></svg>View Reports</li>
    <li><svg width="12" height="12" viewBox="0 0 12 12"><circle cx="6" cy="6" r="6" fill="var(--green)"/><path d="M6 3V9M3 6H9" stroke="#fff" stroke-width="1.6"/></svg>Add Patient</li>
  </ul>
  <div class="completeness">
    <h3>PROFILE COMPLETENESS</h3>
    <svg class="ring" width="68" height="68" viewBox="0 0 68 68">
      <circle cx="34" cy="34" r="30" fill="none" stroke="#eeeeee" stroke-width="5"/>
      <circle cx="34" cy="34" r="30" fill="none" stroke="var(--green)" stroke-width="5" stroke-dasharray="160.2 188.5" transform="rotate(-90 34 34)"/>
      <text x="34" y="43" text-anchor="middle" font-family="Lato,sans-serif" font-weight="700" font-size="26" fill="#111">85</text>
    </svg>
    <ul class="steps"><li>Steps to Completion</li><li>Compare to Others</li><li>More information</li></ul>
  </div>
</section>

<ul class="abs sidemenu" style="top:303px;height:239px;padding-top:10px">
  <li class="active"><svg width="13" height="12" viewBox="0 0 13 12"><path d="M6.5 0L13 6H11V12H8V8H5V12H2V6H0Z" fill="#fff"/></svg>Home</li>
  <li><svg width="14" height="10" viewBox="0 0 14 10"><rect width="14" height="10" fill="#333"/><path d="M0 1L7 6L14 1" fill="none" stroke="#fff"/></svg>Email</li>
  <li><svg width="14" height="12" viewBox="0 0 14 12"><rect x="5" y="0" width="4" height="4" fill="#333"/><rect x="0" y="8" width="4" height="4" fill="#333"/><rect x="5" y="8" width="4" height="4" fill="#333"/><rect x="10" y="8" width="4" height="4" fill="#333"/><path d="M7 4V8M2 8V6H12V8" fill="none" stroke="#333"/></svg>Doctors DB</li>
  <li><svg width="14" height="12" viewBox="0 0 14 12"><circle cx="5" cy="7" r="3.5" fill="none" stroke="#333" stroke-width="2.4" stroke-dasharray="1.8 1"/><circle cx="11" cy="3" r="2.2" fill="none" stroke="#333" stroke-width="1.6"/></svg>Settings</li>
  <li><svg width="14" height="12" viewBox="0 0 14 12"><rect x=".5" y=".5" width="13" height="11" fill="none" stroke="#333"/><path d="M3 10V6M6 10V3M9 10V5M11.5 10V7" stroke="#333" stroke-width="1.6"/></svg>View Chart</li>
  <li><svg width="12" height="12" viewBox="0 0 12 12"><path d="M3.5 3A4.5 4.5 0 1 0 8.5 3" fill="none" stroke="#333" stroke-width="1.6"/><path d="M6 0V6" stroke="#333" stroke-width="1.6"/></svg>Logout</li>
</ul>

<ul class="abs sidemenu" style="top:578px;height:239px">
  <li><svg width="16" height="10" viewBox="0 0 16 10"><path d="M1 10A7 7 0 0 1 15 10" fill="none" stroke="#333" stroke-width="2"/><path d="M8 9L11 4" stroke="#333" stroke-width="2"/></svg>Site Usage</li>
  <li><svg width="14" height="14" viewBox="0 0 14 14"><path d="M3 4A5.5 5.5 0 1 1 2 8" fill="none" stroke="#333" stroke-width="1.8"/><path d="M0 2L3.5 5L5 1Z" fill="#333"/><path d="M7 4V7.5H9.5" fill="none" stroke="#333" stroke-width="1.5"/></svg>Backup</li>
  <li><svg width="16" height="16" viewBox="0 0 16 16"><circle cx="8" cy="8" r="6" fill="none" stroke="#333" stroke-width="4" stroke-dasharray="5 4.4"/></svg>Supports</li>
  <li><svg width="20" height="15" viewBox="0 0 20 15"><ellipse cx="8" cy="6" rx="8" ry="5.5" fill="#333"/><path d="M3 10L1 14L7 11Z" fill="#333"/><ellipse cx="14" cy="9" rx="6" ry="4.5" fill="#333" stroke="#eee"/></svg>New Comments</li>
</ul>

<!-- alerts widget -->
<section class="abs widget" style="left:341px;top:303px">
  <div class="w-head"><b>Latest Abnormal alerts (?)</b><br>as of 10 June 2014</div>
  <div class="w-tools">
    <svg width="11" height="11" viewBox="0 0 11 11"><path d="M9 3A4 4 0 0 0 1.5 4.5M2 8A4 4 0 0 0 9.5 6.5" fill="none" stroke="#222" stroke-width="1.6"/><path d="M10 0V4H6ZM1 11V7H5Z" fill="#222"/></svg>
    <svg width="11" height="11" viewBox="0 0 11 11"><rect x=".5" y="1.5" width="10" height="9" fill="none" stroke="#222"/><rect x=".5" y="1.5" width="10" height="2.5" fill="#222"/><path d="M3 0V2M8 0V2M3 6H8M3 8H8" stroke="#222"/></svg>
    <svg width="10" height="10" viewBox="0 0 10 10"><path d="M1 1L9 9M9 1L1 9" stroke="#222" stroke-width="2.4"/></svg>
  </div>
  <div class="alerts">
    <table>
      <tr><td>21-Apr</td><td style="width:63px">mHS IoT</td><td style="width:76px">BP 141 / 96</td><td>mmHg</td></tr>
      <tr><td>20-Apr</td><td>mHS IoT</td><td>BP 137 / 93</td><td>mmHg</td></tr>
      <tr><td>11-Apr</td><td>Marla K</td><td>BP 151 / 103</td><td>mmHg</td></tr>
      <tr><td>25-Feb</td><td>Marla K</td><td>BP 156 / 97</td><td>mmHg</td></tr>
      <tr><td>18-Feb</td><td>Marla K</td><td>BP 152 / 94</td><td>mmHg</td></tr>
    </table>
  </div>
  <a class="viewall" href="#">View all »</a>
</section>

<svg width="0" height="0" style="position:absolute">
  <defs>
    <radialGradient id="pieGreen" cx="50%" cy="50%" r="50%">
      <stop offset="0" stop-color="#a3d45a"/>
      <stop offset="1" stop-color="#8cc63f"/>
    </radialGradient>
  </defs>
</svg>

<!-- hypertension widget 1 -->
<section class="abs widget" style="left:704px;top:303px">
  <div class="w-head"><b>Hypertension (?)</b><br>from 03 June 2014</div>
  <div class="w-tools">
    <svg width="11" height="11" viewBox="0 0 11 11"><path d="M9 3A4 4 0 0 0 1.5 4.5M2 8A4 4 0 0 0 9.5 6.5" fill="none" stroke="#222" stroke-width="1.6"/><path d="M10 0V4H6ZM1 11V7H5Z" fill="#222"/></svg>
    <svg width="11" height="11" viewBox="0 0 11 11"><rect x=".5" y="1.5" width="10" height="9" fill="none" stroke="#222"/><rect x=".5" y="1.5" width="10" height="2.5" fill="#222"/><path d="M3 0V2M8 0V2M3 6H8M3 8H8" stroke="#222"/></svg>
    <svg width="10" height="10" viewBox="0 0 10 10"><path d="M1 1L9 9M9 1L1 9" stroke="#222" stroke-width="2.4"/></svg>
  </div>
  <svg class="pie" width="166" height="166" viewBox="0 0 166 166">
    <circle cx="83" cy="83" r="83" fill="url(#pieGreen)"/>
    <path d="M83 83V0A83 83 0 0 1 98.1 1.4Z" fill="var(--blue)"/>
    <path d="M83 83L98.1 1.4A83 83 0 0 1 104 2.7Z" fill="var(--yellow)"/>
  </svg>
  <ul class="legend" style="top:106px">
    <li><i style="background:var(--blue)"></i>Normal: 2.91%</li>
    <li><i style="background:var(--yellow)"></i>Threshold: 1.16%</li>
    <li><i style="background:var(--green)"></i>Missed: 95.93%</li>
  </ul>
</section>

<!-- alerts widget 2 -->
<section class="abs widget" style="left:341px;top:578px">
  <div class="w-head"><b>Latest Abnormal alerts (?)</b><br>as of 10 June 2014</div>
  <div class="w-tools">
    <svg width="11" height="11" viewBox="0 0 11 11"><path d="M9 3A4 4 0 0 0 1.5 4.5M2 8A4 4 0 0 0 9.5 6.5" fill="none" stroke="#222" stroke-width="1.6"/><path d="M10 0V4H6ZM1 11V7H5Z" fill="#222"/></svg>
    <svg width="11" height="11" viewBox="0 0 11 11"><rect x=".5" y="1.5" width="10" height="9" fill="none" stroke="#222"/><rect x=".5" y="1.5" width="10" height="2.5" fill="#222"/><path d="M3 0V2M8 0V2M3 6H8M3 8H8" stroke="#222"/></svg>
    <svg width="10" height="10" viewBox="0 0 10 10"><path d="M1 1L9 9M9 1L1 9" stroke="#222" stroke-width="2.4"/></svg>
  </div>
  <svg class="pie" style="left:12px;top:67px" width="166" height="166" viewBox="0 0 166 166">
    <circle cx="83" cy="83" r="83" fill="url(#pieGreen)"/>
  </svg>
  <ul class="legend" style="left:199px;top:138px">
    <li><i style="background:var(--green)"></i>Missed: 100%</li>
  </ul>
</section>

<!-- hypertension widget 2 -->
<section class="abs widget" style="left:704px;top:578px">
  <div class="w-head"><b>Hypertension (?)</b><br>from 03 June 2014</div>
  <div class="w-tools">
    <svg width="11" height="11" viewBox="0 0 11 11"><path d="M9 3A4 4 0 0 0 1.5 4.5M2 8A4 4 0 0 0 9.5 6.5" fill="none" stroke="#222" stroke-width="1.6"/><path d="M10 0V4H6ZM1 11V7H5Z" fill="#222"/></svg>
    <svg width="11" height="11" viewBox="0 0 11 11"><rect x=".5" y="1.5" width="10" height="9" fill="none" stroke="#222"/><rect x=".5" y="1.5" width="10" height="2.5" fill="#222"/><path d="M3 0V2M8 0V2M3 6H8M3 8H8" stroke="#222"/></svg>
    <svg width="10" height="10" viewBox="0 0 10 10"><path d="M1 1L9 9M9 1L1 9" stroke="#222" stroke-width="2.4"/></svg>
  </div>
  <svg class="pie" style="left:12px;top:67px" width="166" height="166" viewBox="0 0 166 166">
    <circle cx="83" cy="83" r="83" fill="url(#pieGreen)"/>
    <path d="M83 83V0A83 83 0 0 1 85.9 0.05Z" fill="var(--yellow)"/>
  </svg>
  <ul class="legend" style="top:130px">
    <li><i style="background:var(--yellow)"></i>Threshold: 0.56%</li>
    <li><i style="background:var(--green)"></i>Missed: 99.44%</li>
  </ul>
</section>

<footer class="abs footer">
  <div class="copy">© 2014 vitalink.example All Rights reserved</div>
  <div class="social"><span></span><span></span><span></span><span></span></div>
</footer>

</body>
</html>
```